Fishing charter business in Sitka Alaska needs new business card design

I have had the same design for 10 plus years, ready for something different. I have attached a copy of my current card and my website link is www.bluecoveangling.net
I am looking for something that will catch my clients eye, although I rely on word of mouth for most of my business a a nice business card will help people remember who I am. My business is located in Sitka Alaska, there are probably 20-30 other charter businesses in Sitka. I like the way my current card is laid out, with the two tone black and grey. I can leave it up to the designers to come up with something else.
Target Market(s)
men, women, couples. Anyone who likes fishing
Industry/Entity Type
Tourism
Contact Information for Business Card
Dorrance's Charter Service
Tidewater Rockline Sportfishing
Colors
Designer to choose colors to be used in the design.
Requirements
Must have
- Gilbert Dorrance
- PO Box 4716
- Sitka, AK 99835
- Compass Rose image
- 100 Ton USCG Licensed Captain
- gdorrance@wavelink.net
- 907-555-0142
- www.bluecoveangling.net
Nice to have
- ghost image of "boat helm"
Should not have
- be to complex

```html
<!DOCTYPE html>
<html lang="en">
<head>
<meta charset="utf-8">
<title>Dorrance's Charter Service – Business Card</title>
<link rel="stylesheet" href="https://fonts.googleapis.com/css2?family=Delius&display=swap">
<style>
  :root {
    --card-bg: #000000;
    --mint: #52efc9;
    --mint-light: #9ff4ee;
    --helm-grey: #36464a;
    --compass-grey: #4a5254;
  }
  html, body {
    margin: 0;
    padding: 0;
    width: 1200px;
    height: 763px;
    overflow: hidden;
    background: var(--card-bg);
  }
  .card {
    position: relative;
    width: 1200px;
    height: 763px;
    background: var(--card-bg);
    overflow: hidden;
    font-family: "Delius", cursive;
    font-style: italic;
    color: var(--mint);
  }
  .helm-area {
    position: absolute;
    left: 777px;
    top: 48px;
    width: 423px;
    height: 715px;
    background: radial-gradient(ellipse 70% 55% at 75% 55%, rgba(54,70,74,0.85) 0%, rgba(54,70,74,0.45) 55%, rgba(54,70,74,0) 100%);
  }
  .compass-area {
    position: absolute;
    left: 96px;
    top: 215px;
    width: 310px;
    height: 317px;
    background: radial-gradient(ellipse at 50% 50%, rgba(82,239,201,0.55) 0%, rgba(74,82,84,0.6) 40%, rgba(74,82,84,0) 72%);
  }
  .business-name, .tagline {
    position: absolute;
    margin: 0;
    font-weight: 400;
    font-size: 36px;
    line-height: 1;
    white-space: nowrap;
    transform: translate(-50%, -50%);
    letter-spacing: 1px;
  }
  .business-name { left: 686px; top: 128px; }
  .tagline { left: 699px; top: 189px; }
  .captain-name {
    position: absolute;
    left: 442px;
    top: 322px;
    margin: 0;
    font-weight: 400;
    font-size: 40px;
    line-height: 1;
    color: var(--mint-light);
    letter-spacing: 1px;
    white-space: nowrap;
  }
  .credential {
    position: absolute;
    left: 449px;
    top: 369px;
    font-size: 15px;
    letter-spacing: 2.6px;
    color: var(--mint-light);
    white-space: nowrap;
  }
  .mailing {
    position: absolute;
    left: 562px;
    top: 451px;
    font-size: 33px;
    line-height: 41px;
    letter-spacing: 1.5px;
    font-style: italic;
    white-space: nowrap;
  }
  .online {
    position: absolute;
    left: 287px;
    top: 614px;
    transform: translateX(-50%);
    text-align: center;
    font-size: 21px;
    line-height: 34px;
    letter-spacing: 0.5px;
    white-space: nowrap;
  }
</style>
</head>
<body>
<main class="card">
  <div class="helm-area" role="img" aria-label="Ghosted grey ship's helm wheel"></div>
  <div class="compass-area" role="img" aria-label="Compass rose in mint and grey"></div>

  <h1 class="business-name">Dorrance's Charter Service</h1>
  <p class="tagline">Tidewater Rockline Sportfishing</p>

  <h2 class="captain-name">Gilbert Dorrance</h2>
  <div class="credential">100 Ton USCG Licensed Captain</div>

  <address class="mailing">
    PO Box 4716<br>
    Sitka, AK 99835<br>
    907-555-0142
  </address>

  <div class="online">
    gdorrance@wavelink.net<br>
    www.bluecoveangling.net
  </div>
</main>
</body>
</html>
```